New letterhead and business cards for dental office

I need a new letterhead, envelopes, and business cards for our 2 dental offices. The letterhead should be able to be used at either office. A professional elegant look is desired.
Exact particulars such as the address, phone numbers etc will be provided later.
***** a reminder: we have 2 separate locations, so the letterhead needs to have 2 sets of addresses, phones numbers, etc.
Our previous letterhead had a check box to indicate which of the two offices we were corresponding from. I would like some creative ideas here.
Industry/Entity Type
Dental
Font styles to use
Look and feel
Each slider illustrates characteristics of the customer's brand and the style your logo design should communicate.

```html
<!DOCTYPE html>
<html lang="en">
<head>
<meta charset="utf-8">
<title>Ashford &amp; Linden Family Dental Centres – Stationery</title>
<link href="https://fonts.googleapis.com/css2?family=Arimo:wght@400;700&display=swap" rel="stylesheet">
<style>
  :root{
    --bg:#e9eaec;
    --paper:#f7f7f8;
    --navy:#2c4585;
    --blue:#3a5ea3;
    --sky:#4d78bf;
    --ink:#2f3f6e;
    --muted:#6d7590;
    --white:#ffffff;
  }
  *{box-sizing:border-box;margin:0;padding:0}
  html,body{width:1200px;height:905px;overflow:hidden}
  body{background:var(--bg);font-family:"Arimo",Arial,sans-serif;color:var(--ink);position:relative}

  .sheet{position:absolute;background:var(--paper);box-shadow:0 2px 6px rgba(0,0,0,.12);overflow:hidden}
  .sheet--blue{background:linear-gradient(135deg,var(--navy) 0%,var(--blue) 60%,var(--sky) 100%)}

  /* brand name block */
  .brand{position:absolute;display:flex;align-items:center;gap:6px}
  .brand__dot{width:12px;height:12px;border-radius:50%;background:currentColor;flex:none}
  .brand__text{display:flex;flex-direction:column}
  .brand__name{font-weight:400;font-size:19px;line-height:1;color:currentColor;border-bottom:1px solid currentColor;padding-bottom:2px}
  .brand__tag{font-size:6px;letter-spacing:2.4px;margin-top:3px;color:currentColor}
  .brand--blue{color:var(--blue)}
  .brand--white{color:var(--white)}

  .decor{position:absolute}
  .decor--light{background:radial-gradient(ellipse at 50% 30%,rgba(180,186,200,.35),rgba(180,186,200,0) 70%)}
  .decor--dark{background:radial-gradient(ellipse at 50% 60%,rgba(255,255,255,.14),rgba(255,255,255,0) 70%)}

  .doctors{position:absolute;font-size:6px;line-height:1.5;color:var(--muted)}

  /* office blocks with selection box */
  .office{position:absolute;display:flex;gap:6px;font-size:5.5px;line-height:1.45;color:var(--ink)}
  .office__box{width:10px;height:10px;border:1px solid var(--ink);flex:none;margin-top:1px}
  .office__title{font-weight:700;font-size:5.5px;letter-spacing:.3px}
  .office--right{flex-direction:row-reverse;text-align:right}

  .band{position:absolute;left:0;right:0;bottom:0;height:7px;display:flex}
  .band__left{flex:1;background:var(--sky)}
  .band__right{flex:1;background:var(--navy)}

  /* positions */
  .letterhead{left:40px;top:40px;width:360px;height:509px}
  .folder{left:430px;top:40px;width:360px;height:509px}
  .card-back{left:830px;top:40px;width:330px;height:190px}
  .card-front{left:830px;top:260px;width:330px;height:190px}
  .env-back{left:40px;top:600px;width:545px;height:260px}
  .env-front{left:615px;top:600px;width:545px;height:260px}

  .card-name{position:absolute;font-size:8px;font-weight:700;letter-spacing:.5px;color:var(--ink)}
  .card-role{position:absolute;font-size:6.5px;color:var(--muted)}

  .flap{position:absolute;left:0;right:0;top:0;height:80px;background:linear-gradient(90deg,var(--navy),var(--sky));border-bottom-right-radius:18px}
  .seal{position:absolute;width:12px;height:12px;border-radius:50%;background:var(--blue)}
</style>
</head>
<body>

<!-- Letterhead -->
<section class="sheet letterhead">
  <div class="decor decor--light" style="right:20px;top:0;width:170px;height:140px" role="img" aria-label="Faint abstract swoosh figures decoration"></div>
  <div class="brand brand--blue" style="left:28px;top:70px">
    <span class="brand__dot"></span>
    <div class="brand__text"><span class="brand__name">Ashford &amp; Linden</span><span class="brand__tag">FAMILY DENTAL CENTRES</span></div>
  </div>
  <p class="doctors" style="left:46px;top:110px">Dr. Helen Marsh, DDS<br>Dr. Owen Pryce, DMD<br>&amp; Associates</p>
  <div class="office office--right" style="right:22px;bottom:86px">
    <span class="office__box"></span>
    <div><div class="office__title">LINDEN FAMILY DENTAL CENTRE</div>82 Grove Street, Linden ON K0A 2C0<br>Tel 613 555 0178 &nbsp;Fax 613 555 0179<br>lindendental.example</div>
  </div>
  <div class="office" style="left:22px;bottom:24px">
    <span class="office__box"></span>
    <div><div class="office__title">ASHFORD FAMILY DENTAL</div>14 Mill Road, Ashford ON K0A 1B0<br>Tel 613 555 0142 &nbsp;Fax 613 555 0143<br>ashforddental.example</div>
  </div>
  <div class="band"><span class="band__left"></span><span class="band__right"></span></div>
</section>

<!-- Folder cover -->
<section class="sheet sheet--blue folder">
  <div class="brand brand--white" style="left:110px;top:60px">
    <span class="brand__dot"></span>
    <div class="brand__text"><span class="brand__name">Ashford &amp; Linden</span><span class="brand__tag">FAMILY DENTAL CENTRES</span></div>
  </div>
  <div class="decor decor--dark" style="left:40px;top:230px;width:260px;height:279px" role="img" aria-label="Faint abstract swoosh figures decoration"></div>
</section>

<!-- Business card back -->
<section class="sheet sheet--blue card-back">
  <div class="decor decor--dark" style="left:0;top:20px;width:150px;height:170px" role="img" aria-label="Faint abstract swoosh figures decoration"></div>
  <div class="brand brand--white" style="left:140px;top:70px">
    <span class="brand__dot"></span>
    <div class="brand__text"><span class="brand__name">Ashford &amp; Linden</span><span class="brand__tag">FAMILY DENTAL CENTRES</span></div>
  </div>
</section>

<!-- Business card front -->
<section class="sheet card-front">
  <div class="brand brand--blue" style="left:22px;top:28px">
    <span class="brand__dot"></span>
    <div class="brand__text"><span class="brand__name">Ashford &amp; Linden</span><span class="brand__tag">FAMILY DENTAL CENTRES</span></div>
  </div>
  <p class="card-name" style="left:40px;top:82px">DR. HELEN MARSH</p>
  <p class="card-role" style="left:40px;top:94px">Dentist</p>
  <div class="office" style="left:22px;bottom:22px">
    <div><div class="office__title">ASHFORD FAMILY DENTAL</div>14 Mill Road, Ashford ON K0A 1B0<br>Tel 613 555 0142<br>ashforddental.example</div>
  </div>
  <div class="office office--right" style="right:22px;bottom:22px">
    <div><div class="office__title">LINDEN FAMILY DENTAL CENTRE</div>82 Grove Street, Linden ON K0A 2C0<br>Tel 613 555 0178<br>lindendental.example</div>
  </div>
  <div class="band"><span class="band__left"></span><span class="band__right"></span></div>
</section>

<!-- Envelope back -->
<section class="sheet env-back">
  <div class="flap"></div>
  <span class="seal" style="left:266px;top:118px"></span>
</section>

<!-- Envelope front -->
<section class="sheet env-front">
  <div class="decor decor--light" style="right:30px;top:0;width:160px;height:110px" role="img" aria-label="Faint abstract swoosh figures decoration"></div>
  <div class="brand brand--blue" style="left:36px;top:96px">
    <span class="brand__dot"></span>
    <div class="brand__text"><span class="brand__name">Ashford &amp; Linden</span><span class="brand__tag">FAMILY DENTAL CENTRES</span></div>
  </div>
  <div class="office office--right" style="right:22px;top:24px">
    <span class="office__box"></span>
    <div><div class="office__title">LINDEN FAMILY DENTAL CENTRE</div>82 Grove Street, Linden ON K0A 2C0<br>Tel 613 555 0178</div>
  </div>
  <div class="office" style="left:22px;bottom:22px">
    <span class="office__box"></span>
    <div><div class="office__title">ASHFORD FAMILY DENTAL</div>14 Mill Road, Ashford ON K0A 1B0<br>Tel 613 555 0142</div>
  </div>
  <div class="band"><span class="band__left"></span><span class="band__right"></span></div>
</section>

</body>
</html>
```